New Web Design Project

Details for my new Web Design Project will be added soon.
Updates
This is my website that need to be work into it www.marlowesquest.com
I am really frustrated with your company, we really need a refund of $556.00 as soon as possible, Do not feel safe to work with.

```html
<!DOCTYPE html>
<html lang="en">
<head>
<meta charset="utf-8">
<title>Marlowe's Quest</title>
<link rel="stylesheet" href="https://fonts.googleapis.com/css2?family=Open+Sans:wght@300;400;600;700&family=Roboto:wght@300;400;500&display=swap">
<style>
:root{
  --topbar:#2d2842;
  --header:#4a3f6b;
  --red:#e8503a;
  --red-dark:#d3432f;
  --page:#e9e9eb;
  --white:#ffffff;
  --ink:#333333;
  --muted:#777777;
  --pink:#f06c6c;
  --btn-pink:#f7a3a3;
  --dark:#3a3a3a;
  --sale:#7fd3d8;
  --footer-link:#8a82a8;
  --social:#3b5a9a;
}
*{margin:0;padding:0;box-sizing:border-box}
html,body{width:1200px;height:2176px;overflow:hidden}
body{font-family:"Open Sans",Arial,sans-serif;background:var(--page);color:var(--ink);position:relative}
.abs{position:absolute}
.topbar{left:0;top:0;width:1200px;height:48px;background:var(--topbar)}
.topbar nav{position:absolute;left:45px;top:17px;display:flex;gap:22px;font-size:10px;letter-spacing:.3px;color:#9a93b8;text-transform:uppercase}
.topbar nav a:first-child{color:#fff;font-weight:600}
.topbar .prefs{position:absolute;right:48px;top:16px;font-size:11px;color:#fff;display:flex;gap:44px;font-weight:600}
.header{left:0;top:48px;width:1200px;height:211px;background:var(--header)}
.brand{left:52px;top:76px;font-size:52px;font-weight:300;color:#fff;letter-spacing:-.5px;white-space:nowrap}
.phone{left:683px;top:108px;display:flex;align-items:center;gap:10px;font-family:Roboto,sans-serif;font-weight:300;font-size:29px;color:#a59fc0;white-space:nowrap}
.cart{left:958px;top:106px;width:204px;height:42px;background:var(--red);color:#fff;font-size:11px;display:flex;align-items:center;padding-left:14px;gap:8px;white-space:nowrap}
.cart b{font-weight:600}
.cart span{color:#ffd2c9}
.mainnav{left:45px;top:179px;width:1118px;height:80px;background:var(--red);display:flex}
.mainnav a{width:166px;border-right:1px solid #f3846f;color:#fff;font-size:13px;display:flex;align-items:center;justify-content:center;text-transform:uppercase}
.search{position:absolute;right:12px;top:20px;width:236px;height:40px;background:var(--red-dark);color:#f7b3a6;font-size:12px;padding:12px 10px}
.search svg{position:absolute;right:10px;top:9px}
.panel{background:var(--white)}
.slider{left:45px;top:267px;width:739px;height:543px}
.slide-img{left:13px;top:13px;width:715px;height:518px;background:linear-gradient(90deg,#d9d9d9,#efefef 60%,#e3e3e3)}
.slide-model{left:30px;top:24px;width:240px;height:480px;background:linear-gradient(180deg,#2b2b2b,#111);border-radius:20px}
.slide-text{left:264px;top:166px;width:460px;font-family:Roboto,sans-serif;font-weight:300;font-size:46px;line-height:62px;text-align:center;color:#333;white-space:nowrap}
.slide-text .hl{color:#e02a2a}
.arrow{top:255px;width:40px;height:42px;background:#888;opacity:.85;display:flex;align-items:center;justify-content:center}
.promo{left:811px;width:352px;height:256px;padding:13px}
.promo-img{width:100%;height:100%;position:relative;padding:38px 42px;color:#fff}
.promo-ship{background:linear-gradient(135deg,#8c86a4,#6e6a8a)}
.promo-wed{background:linear-gradient(135deg,#e7604d,#cf4a3a)}
.promo h3{font-family:Roboto,sans-serif;font-weight:500;font-size:46px;line-height:46px}
.promo p{font-size:14px;font-weight:600;margin-top:6px}
.cat{top:830px;height:154px;background:linear-gradient(180deg,#fff,#f1f1f1)}
.cat-img{left:12px;top:8px;width:130px;height:140px}
.cat-title{left:145px;top:42px;width:210px;text-align:center;font-family:Roboto,sans-serif;font-weight:300;font-size:23px;line-height:28px;color:#333;white-space:nowrap}
.cat-link{right:18px;top:104px;font-size:21px;color:var(--pink);font-family:Roboto,sans-serif;font-weight:300;display:flex;align-items:center;gap:8px}
.specials{left:42px;top:1002px;width:1121px;height:497px}
.specials h2{position:absolute;left:26px;top:14px;font-size:16px;font-weight:600;text-transform:uppercase;color:#333}
.specials hr{position:absolute;left:26px;top:42px;width:1070px;border:0;border-top:1px solid #ccc}
.product{top:67px;width:250px;text-align:center}
.product .img{margin:0 auto;width:195px;height:278px}
.sale{position:absolute;right:12px;top:-7px;width:22px;height:54px;background:var(--sale);color:#fff;font-size:9px;writing-mode:vertical-rl;transform:rotate(180deg);display:flex;align-items:center;justify-content:center}
.product h4{font-size:12px;font-weight:400;color:var(--pink);line-height:19px;margin-top:17px}
.product .desc{font-size:10px;color:#444;margin-top:2px}
.price{font-size:16px;margin-top:5px}
.price s{color:#555;margin-right:6px}
.price b{color:var(--pink);font-weight:400}
.btns{margin-top:9px;display:flex;justify-content:center;gap:4px}
.btns span{font-size:11px;padding:6px 8px;color:#fff}
.add{background:var(--btn-pink)}
.det{background:var(--dark)}
.box-head{height:64px;background:#3c3c3c;color:#fff;font-family:Roboto,sans-serif;font-weight:300;font-size:30px;padding:12px 26px}
.reasons{left:42px;top:1509px;width:760px;height:296px;background:linear-gradient(180deg,#fff,#efefef)}
.reasons .body{padding:20px 20px;font-size:13px;line-height:18px;color:#444}
.follow{left:813px;top:1509px;width:352px;height:312px;background:linear-gradient(180deg,#fff,#efefef)}
.follow .body{padding:24px 21px;font-size:17px;color:#999;line-height:25px;font-weight:300}
.social{display:inline-flex;align-items:center;gap:5px;color:var(--social);font-size:13px;font-weight:600;vertical-align:middle;margin-left:4px}
.social i{width:12px;height:12px;background:var(--social);display:inline-block}
.store-badge{position:absolute;left:21px;top:183px;width:292px;height:126px;background:#7c3fc7}
.ship-band{left:32px;top:1840px;width:1141px;height:112px;background:linear-gradient(90deg,#3a3a3a,#6a6a6a 45%,#333)}
.ship-band .lbl{position:absolute;left:98px;top:36px;font-family:Roboto,sans-serif;font-size:34px;color:#222;-webkit-text-stroke:1px #ddd;white-space:nowrap}
.ship-band .txt{position:absolute;left:576px;top:16px;width:540px;font-size:14.5px;line-height:19px;color:#fff}
.footer{left:0;top:1971px;width:1200px;height:205px;background:var(--header)}
.fcol{top:20px;color:#fff}
.fcol h5{font-size:16px;font-weight:600;margin-bottom:12px}
.fcol ul{list-style:none;font-size:11.5px;line-height:16.5px;color:var(--footer-link)}
.newsletter input{width:136px;height:22px;border:0;background:#fff;display:inline-block;vertical-align:middle}
.newsletter .go{display:inline-flex;width:36px;height:22px;background:var(--red);vertical-align:middle;align-items:center;justify-content:center}
.callus{font-size:14px;margin-top:26px}
.callus span{color:var(--pink)}
.copy{left:29px;top:2144px;font-size:11px;color:#6e6790}
.payname{left:1083px;top:2140px;font-size:12px;font-weight:600;color:#cfc9e3}
</style>
</head>
<body>

<div class="abs topbar">
  <nav><a>Home</a><a>Wish List (0)</a><a>My Account</a><a>Shopping Cart</a><a>Checkout</a><a>Login</a><a>Create an Account</a></nav>
  <div class="prefs"><span>$ ▾</span><span>En ▾</span></div>
</div>

<header class="abs header"></header>
<div class="abs brand">Marlowe's Quest</div>
<div class="abs phone">
  <svg width="30" height="30" viewBox="0 0 24 24"><path fill="#e8503a" d="M6.6 10.8a15.1 15.1 0 0 0 6.6 6.6l2.2-2.2c.3-.3.7-.4 1-.2 1.1.4 2.3.6 3.6.6.6 0 1 .4 1 1V20c0 .6-.4 1-1 1A17 17 0 0 1 3 4c0-.6.4-1 1-1h3.5c.6 0 1 .4 1 1 0 1.3.2 2.5.6 3.6.1.3 0 .7-.2 1z"/></svg>
  1-800-555-0142
</div>
<div class="abs cart">
  <svg width="18" height="16" viewBox="0 0 24 20"><path d="M0 1h4l3 11h13l3-8H7" stroke="#fff" stroke-width="2" fill="none"/><circle cx="9" cy="17" r="2" fill="#fff"/><circle cx="19" cy="17" r="2" fill="#fff"/></svg>
  <b>Cart:</b><span>0 ITEM(S) - $0.00</span><span style="margin-left:auto;margin-right:12px;color:#fff">▾</span>
</div>

<nav class="abs mainnav">
  <a>Home</a><a>About Us</a><a>Showroom</a><a>Privacy Policy</a><a>View Cart</a>
  <div class="search">Search
    <svg width="22" height="22" viewBox="0 0 24 24"><circle cx="10" cy="10" r="7" stroke="#f7b3a6" stroke-width="3" fill="none"/><path d="M15 15l6 6" stroke="#f7b3a6" stroke-width="3"/></svg>
  </div>
</nav>

<section class="abs panel slider">
  <div class="abs slide-img">
    <div class="abs slide-model" role="img" aria-label="Model wearing black skirtpants yoga capri"></div>
    <div class="abs slide-text">SKIRTPANTS<br><span class="hl">YOGA CAPRI ALL</span><br>BLACK MQYP03</div>
  </div>
  <div class="abs arrow" style="left:0"><svg width="12" height="18"><path d="M10 2L3 9l7 7" stroke="#fff" stroke-width="2" fill="none"/></svg></div>
  <div class="abs arrow" style="right:0"><svg width="12" height="18"><path d="M2 2l7 7-7 7" stroke="#fff" stroke-width="2" fill="none"/></svg></div>
</section>

<aside class="abs panel promo" style="top:267px">
  <div class="promo-img promo-ship" role="img" aria-label="Gift boxes background">
    <h3>FREE<br><span style="color:#4a3f6b">SHIPPING</span></h3>
    <p>ON ORDERS OVER $99</p>
  </div>
</aside>
<aside class="abs panel promo" style="top:554px">
  <div class="promo-img promo-wed" role="img" aria-label="Wedding accessories background">
    <h3 style="font-size:40px;line-height:40px">WEDDING<br><span style="color:#7a2a22">ACCESSORIES</span></h3>
    <p>SAVE UP TO</p>
    <div style="font-family:Roboto,sans-serif;font-weight:300;font-size:90px;line-height:90px;color:#f3b0a4">20%</div>
  </div>
</aside>

<div class="abs cat" style="left:42px;width:371px">
  <div class="abs cat-img" style="background:linear-gradient(135deg,#f06fa0,#5fb6e6,#f6d24c)" role="img" aria-label="Printed skating skirt"></div>
  <div class="abs cat-title">SHORTS &amp; SKIRTS</div>
  <div class="abs cat-link">Shop Now <svg width="18" height="18" viewBox="0 0 20 20"><circle cx="10" cy="10" r="8" stroke="#999" stroke-width="2" fill="none"/><path d="M8 6l4 4-4 4" stroke="#999" stroke-width="2" fill="none"/></svg></div>
</div>
<div class="abs cat" style="left:416px;width:370px">
  <div class="abs cat-img" style="background:linear-gradient(180deg,#d8d8d8,#f7f7f7)" role="img" aria-label="White competition skating dress"></div>
  <div class="abs cat-title" style="left:130px;width:240px">COMPETITION ICE<br>FIGURE SKATING</div>
  <div class="abs cat-link">Shop Now <svg width="18" height="18" viewBox="0 0 20 20"><circle cx="10" cy="10" r="8" stroke="#999" stroke-width="2" fill="none"/><path d="M8 6l4 4-4 4" stroke="#999" stroke-width="2" fill="none"/></svg></div>
</div>
<div class="abs cat" style="left:789px;width:374px">
  <div class="abs cat-img" style="background:linear-gradient(135deg,#5a22c8,#2a0d7a)" role="img" aria-label="Purple skate boot cover"></div>
  <div class="abs cat-title">BOOT COVER</div>
  <div class="abs cat-link">Shop Now <svg width="18" height="18" viewBox="0 0 20 20"><circle cx="10" cy="10" r="8" stroke="#999" stroke-width="2" fill="none"/><path d="M8 6l4 4-4 4" stroke="#999" stroke-width="2" fill="none"/></svg></div>
</div>

<section class="abs panel specials">
  <h2>Special Products</h2>
  <hr>
  <div class="abs product" style="left:26px">
    <div class="img" style="background:linear-gradient(180deg,#f2f2f2,#e88070 40%,#6b4b3e)" role="img" aria-label="Woman in coral henley top"></div>
    <div class="sale">SALE</div>
    <h4>Fortune Lane Women's Plus-Size<br>Sienna Button Henley</h4>
    <div class="desc">In our Plus Size Women's Clothing Store ...</div>
    <div class="price"><s>$33.33</s><b>$30.00</b></div>
    <div class="btns"><span class="add">Add to Cart</span><span class="det">Details</span></div>
  </div>
  <div class="abs product" style="left:301px">
    <div class="img" style="background:linear-gradient(180deg,#f2f2f2,#a08058 35%,#1e1e1e 45%,#151515)" role="img" aria-label="Woman in black stretch pants with printed waistband"></div>
    <div class="sale">SALE</div>
    <h4>Eastpeak Juniors Plus-Size Printed<br>Waist Stretch Pant With Stud Trim</h4>
    <div class="desc">In our Plus Size Women's Clothing Store ...</div>
    <div class="price"><s>$25.33</s><b>$22.00</b></div>
    <div class="btns"><span class="add">Add to Cart</span><span class="det">Details</span></div>
  </div>
  <div class="abs product" style="left:576px">
    <div class="img" style="background:linear-gradient(180deg,#f2f2f2,#9ea6a3 40%,#3a3a3a)" role="img" aria-label="Woman in grey cowl neck top"></div>
    <div class="sale">SALE</div>
    <h4>Neon Lotus Women's Plus-Size<br>Soft Drape Cowl</h4>
    <div class="desc">Specially for your comfort, we created a ...</div>
    <div class="price"><s>$46.30</s><b>$40.00</b></div>
    <div class="btns"><span class="add">Add to Cart</span><span class="det">Details</span></div>
  </div>
  <div class="abs product" style="left:851px">
    <div class="img" style="background:linear-gradient(180deg,#f2f2f2,#b02a6a 40%,#3a3550)" role="img" aria-label="Woman in pink striped wrap neck top"></div>
    <div class="sale">SALE</div>
    <h4>Mira Lenz Women's Plus-Size Wave<br>Stripe Wrap Neck Top</h4>
    <div class="desc">Specially for your comfort, we created a ...</div>
    <div class="price"><s>$55.30</s><b>$50.00</b></div>
    <div class="btns"><span class="add">Add to Cart</span><span class="det">Details</span></div>
  </div>
</section>

<section class="abs reasons">
  <div class="box-head">Reasons to shop from us</div>
  <div class="body">
    Thank you for your interest in Marlowe's Quest, Inc. products.<br>
    Marlowe's Quest specializes in designing and creating high-end designed competition figure skating dresses and costumes for figure skaters including baton twirling, majorettes, drill team uniforms, or dancer costumes in United States.<br>
    We are local maufacturer of quality skate and sportswear and are based in the United States.<br>
    We are proudly manufacture all our products here, however, we specialize both in domestic as well as international orders.<br>
    For wholesale please contact us either by phone or email for more information.<br><br>
    Like US @ www.linkwall.com/marlowesquest
  </div>
</section>

<section class="abs follow">
  <div class="box-head">Follow Us :</div>
  <div class="body">Like US @ <span class="social"><i></i>Linkwall</span><br>www.linkwall.com/marlowesquest</div>
  <div class="store-badge" role="img" aria-label="Store platform badge"></div>
</section>

<section class="abs ship-band">
  <div class="lbl">SHIPPING COST: 35% CODE :</div>
  <div class="txt">(MQSAVE2014)!!!!!!!!!! Free Domestic Buyers + 35% Discount! $5.99 Canada Buyers + 35% Discount! $9.99 Worldwide Buyers + 35% Discount! Please Like US @ https://www.linkwall.com/marlowesquest</div>
</section>

<footer class="abs footer">
  <div class="abs fcol" style="left:73px"><h5>Information</h5><ul><li>Home</li><li>About Us</li><li>Products</li><li>Enquiry</li><li>Contacts</li></ul></div>
  <div class="abs fcol" style="left:339px"><h5>Why buy from us</h5><ul><li>Shipping &amp; Returns</li><li>Secure Shopping</li><li>International Shipping</li><li>Affiliates</li><li>Group Sales</li></ul></div>
  <div class="abs fcol" style="left:634px"><h5>My account</h5><ul><li>Sign In</li><li>View Cart</li><li>My Wishlist</li><li>Track My Order</li><li>Help</li></ul></div>
  <div class="abs fcol newsletter" style="left:906px"><h5 style="font-size:14px">Newsletter</h5>
    <input type="text" aria-label="Email"><span class="go"><svg width="10" height="10"><path d="M3 1l4 4-4 4" stroke="#fff" stroke-width="2" fill="none"/></svg></span>
    <div class="callus">Call us: <span>(800) 555-0199</span></div>
  </div>
</footer>
<div class="abs copy">© 2014 marlowesquest.com. All Rights Reserved</div>
<div class="abs payname">Cashford</div>

</body>
</html>
```